Bold and colurful E-liquid Design Template

I'm looking for a new label for my house range of vape e-liquids. I currently have almost 40 flavours, so I'm looking for a single label design that I can modify to create the rest of the flavours.
Each label will have the same design, but I'll change the color for each flavour and the name.
I'd like the label to be predominantly text based with bold text and bold colours. I like bold typographic styles. Also for each flavour I'd like to add 1 - 3 letters to represent the flavour. This can be in a larger font.
eg for
Blueberry I'll use the letter B
Pineapple Peach will use PP
Cinnamon Blueberry Muffin uses CBM
The colour used on the label will also be important so they stand out nicely on the shelf.
I've attached a psd mockup of the bottles I'll be using.

```html
<!DOCTYPE html>
<html lang="en">
<head>
<meta charset="utf-8">
<title>E-Liquid Label Range</title>
<link href="https://fonts.googleapis.com/css2?family=DM+Serif+Display&family=Dosis:wght@500&family=Montserrat:wght@400;700&display=swap" rel="stylesheet">
<style>
  :root {
    --page: #e9eaea;
    --label-bg: #0d0e10;
    --ink: #ffffff;
    --body-ink: #e6e6e6;
    --cinnamon: #f6b53a;
    --cinnamon-smoke: #d9914a;
    --blueberry: #2aa6e0;
    --blueberry-smoke: #1f7fd0;
    --pineapple: #f2d414;
    --pineapple-smoke: #d9bf1e;
  }
  * { margin: 0; padding: 0; box-sizing: border-box; }
  html, body { width: 1200px; height: 1061px; overflow: hidden; background: var(--page); }
  .range {
    position: relative; width: 1200px; height: 1061px;
    display: flex; justify-content: center; align-items: center; gap: 21px;
  }
  .label {
    position: relative; width: 372px; height: 314px; overflow: hidden;
    background: var(--label-bg); color: var(--ink);
  }
  .label--cinnamon { --accent: var(--cinnamon); --smoke: var(--cinnamon-smoke); }
  .label--blueberry { --accent: var(--blueberry); --smoke: var(--blueberry-smoke); }
  .label--pineapple { --accent: var(--pineapple); --smoke: var(--pineapple-smoke); }

  .smoke {
    position: absolute; left: 0; top: 0; width: 170px; height: 314px;
    background: radial-gradient(ellipse 60% 35% at 80% 8%, color-mix(in srgb, var(--smoke) 70%, transparent), transparent 70%),
                radial-gradient(ellipse 55% 40% at 25% 70%, color-mix(in srgb, var(--smoke) 65%, transparent), transparent 75%),
                radial-gradient(ellipse 40% 30% at 60% 40%, color-mix(in srgb, var(--smoke) 40%, transparent), transparent 75%);
  }
  .smoke--corner {
    left: auto; right: 0; top: auto; bottom: 0; width: 70px; height: 130px;
    background: radial-gradient(ellipse 60% 60% at 80% 70%, color-mix(in srgb, var(--smoke) 55%, transparent), transparent 75%);
  }
  .flavour {
    position: absolute; top: 36px; left: 60px;
    writing-mode: vertical-rl;
    font-family: "DM Serif Display", serif; font-size: 46px; line-height: 0.82;
    white-space: nowrap;
  }
  .label--cinnamon .flavour { left: 60px; top: 22px; font-size: 37px; }
  .label--blueberry .flavour { left: 64px; top: 56px; }
  .label--pineapple .flavour { left: 64px; top: 46px; }

  .spec {
    position: absolute; bottom: 6px;
    font-family: "Dosis", sans-serif; font-weight: 500; font-size: 15px;
  }
  .spec--volume { left: 30px; }
  .spec--strength { left: 117px; }

  .info { position: absolute; left: 175px; top: 10px; width: 190px; font-family: "Montserrat", sans-serif; }
  .info__title {
    color: var(--accent); font-weight: 700; font-size: 10.5px; letter-spacing: 0.01em;
    padding-bottom: 3px; border-bottom: 1.5px solid #cfcfcf; margin-right: -8px;
  }
  .info__section { margin-top: 11px; }
  .info__section + .info__section { margin-top: 8px; }
  .info__heading { color: var(--accent); font-weight: 700; font-size: 9px; line-height: 1.1; }
  .info__text { color: var(--body-ink); font-size: 7.2px; line-height: 1.32; letter-spacing: -0.01em; }
  .info__text--caps { text-transform: uppercase; }

  .icons { position: absolute; left: 210px; top: 228px; display: flex; gap: 14px; align-items: center; }
  .footer {
    position: absolute; bottom: 14px; left: 182px; right: 22px;
    display: flex; justify-content: space-between; align-items: flex-end;
    font-family: "Montserrat", sans-serif; font-weight: 700; font-size: 6px; line-height: 1.2;
  }
  .footer__origin { text-align: center; }
</style>
</head>
<body>
<main class="range">

  <article class="label label--cinnamon">
    <div class="smoke" role="img" aria-label="Wisps of amber smoke drifting up the label"></div>
    <div class="smoke smoke--corner" role="img" aria-label="Amber smoke wisp in the corner"></div>
    <h2 class="flavour">Cinnamon<br>Blueberry Muffin</h2>
    <span class="spec spec--volume">60ML</span>
    <span class="spec spec--strength">6MG</span>
    <div class="info">
      <p class="info__title">PREMEMUM&nbsp; E-LIQUID</p>
      <section class="info__section">
        <h3 class="info__heading">INGREDIENTS:</h3>
        <p class="info__text"><span class="info__text--caps">Vegetable glycerin, propylene glycol<br>natural &amp; artificial flavor 3%<br>nicotine by volume</span><br>May contain trace elements of nuts or seeds</p>
      </section>
      <section class="info__section">
        <h3 class="info__heading">WARNING:</h3>
        <p class="info__text">This product contains nicotine, a chemical known to the State of California to cause birth defects or other reproductive harm.<br>This product is for adult use only. Keep away from children and pets. Do not ingest or apply to the skin. If nicotine poisoning occurs seek immediate medical attention.</p>
      </section>
      <section class="info__section">
        <h3 class="info__heading">USE WITH CAUTION:</h3>
        <p class="info__text">Lorem ipsum dolor sit amet, consectetur adipisicing elit, sed do eiusmod tempor incididunt ut labore et dolore magna aliqua. Ut enim ad minim veniam, quis nostrud exercitation ullamco</p>
      </section>
    </div>
    <div class="icons">
      <svg width="18" height="18" viewBox="0 0 20 20" aria-label="Poison"><circle cx="10" cy="7" r="5" fill="#fff"/><path d="M3 12l14 6M17 12L3 18" stroke="#fff" stroke-width="2.2" stroke-linecap="round"/></svg>
      <svg width="20" height="18" viewBox="0 0 22 20" aria-label="Warning"><path d="M11 1L21 19H1Z" fill="#fff"/><path d="M11 7v6" stroke="#0d0e10" stroke-width="2.2"/><circle cx="11" cy="16" r="1.2" fill="#0d0e10"/></svg>
      <svg width="16" height="18" viewBox="0 0 16 20" aria-label="Dispose properly"><path d="M3 8h10l-1.2 11H4.2Z" fill="none" stroke="#fff" stroke-width="1.4"/><path d="M2 6h12M8 1v4M5.5 3L8 1l2.5 2" fill="none" stroke="#fff" stroke-width="1.4"/></svg>
    </div>
    <div class="footer"><span>MANUFACTURED BY:</span><span class="footer__origin">MADE IN<br>NEW ZEALAND</span></div>
  </article>

  <article class="label label--blueberry">
    <div class="smoke" role="img" aria-label="Wisps of blue smoke drifting up the label"></div>
    <div class="smoke smoke--corner" role="img" aria-label="Blue smoke wisp in the corner"></div>
    <h2 class="flavour">Blueberry</h2>
    <span class="spec spec--volume">60ML</span>
    <span class="spec spec--strength">6MG</span>
    <div class="info">
      <p class="info__title">PREMEMUM&nbsp; E-LIQUID</p>
      <section class="info__section">
        <h3 class="info__heading">INGREDIENTS:</h3>
        <p class="info__text"><span class="info__text--caps">Vegetable glycerin, propylene glycol<br>natural &amp; artificial flavor 3%<br>nicotine by volume</span><br>May contain trace elements of nuts or seeds</p>
      </section>
      <section class="info__section">
        <h3 class="info__heading">WARNING:</h3>
        <p class="info__text">This product contains nicotine, a chemical known to the State of California to cause birth defects or other reproductive harm.<br>This product is for adult use only. Keep away from children and pets. Do not ingest or apply to the skin. If nicotine poisoning occurs seek immediate medical attention.</p>
      </section>
      <section class="info__section">
        <h3 class="info__heading">USE WITH CAUTION:</h3>
        <p class="info__text">Lorem ipsum dolor sit amet, consectetur adipisicing elit, sed do eiusmod tempor incididunt ut labore et dolore magna aliqua. Ut enim ad minim veniam, quis nostrud exercitation ullamco</p>
      </section>
    </div>
    <div class="icons">
      <svg width="18" height="18" viewBox="0 0 20 20" aria-label="Poison"><circle cx="10" cy="7" r="5" fill="#fff"/><path d="M3 12l14 6M17 12L3 18" stroke="#fff" stroke-width="2.2" stroke-linecap="round"/></svg>
      <svg width="20" height="18" viewBox="0 0 22 20" aria-label="Warning"><path d="M11 1L21 19H1Z" fill="#fff"/><path d="M11 7v6" stroke="#0d0e10" stroke-width="2.2"/><circle cx="11" cy="16" r="1.2" fill="#0d0e10"/></svg>
      <svg width="16" height="18" viewBox="0 0 16 20" aria-label="Dispose properly"><path d="M3 8h10l-1.2 11H4.2Z" fill="none" stroke="#fff" stroke-width="1.4"/><path d="M2 6h12M8 1v4M5.5 3L8 1l2.5 2" fill="none" stroke="#fff" stroke-width="1.4"/></svg>
    </div>
    <div class="footer"><span>MANUFACTURED BY:</span><span class="footer__origin">MADE IN<br>NEW ZEALAND</span></div>
  </article>

  <article class="label label--pineapple">
    <div class="smoke" role="img" aria-label="Wisps of yellow smoke drifting up the label"></div>
    <div class="smoke smoke--corner" role="img" aria-label="Yellow smoke wisp in the corner"></div>
    <h2 class="flavour">Pineapple</h2>
    <span class="spec spec--volume">60ML</span>
    <span class="spec spec--strength">6MG</span>
    <div class="info">
      <p class="info__title">PREMEMUM&nbsp; E-LIQUID</p>
      <section class="info__section">
        <h3 class="info__heading">INGREDIENTS:</h3>
        <p class="info__text"><span class="info__text--caps">Vegetable glycerin, propylene glycol<br>natural &amp; artificial flavor 3%<br>nicotine by volume</span><br>May contain trace elements of nuts or seeds</p>
      </section>
      <section class="info__section">
        <h3 class="info__heading">WARNING:</h3>
        <p class="info__text">This product contains nicotine, a chemical known to the State of California to cause birth defects or other reproductive harm.<br>This product is for adult use only. Keep away from children and pets. Do not ingest or apply to the skin. If nicotine poisoning occurs seek immediate medical attention.</p>
      </section>
      <section class="info__section">
        <h3 class="info__heading">USE WITH CAUTION:</h3>
        <p class="info__text">Lorem ipsum dolor sit amet, consectetur adipisicing elit, sed do eiusmod tempor incididunt ut labore et dolore magna aliqua. Ut enim ad minim veniam, quis nostrud exercitation ullamco</p>
      </section>
    </div>
    <div class="icons">
      <svg width="18" height="18" viewBox="0 0 20 20" aria-label="Poison"><circle cx="10" cy="7" r="5" fill="#fff"/><path d="M3 12l14 6M17 12L3 18" stroke="#fff" stroke-width="2.2" stroke-linecap="round"/></svg>
      <svg width="20" height="18" viewBox="0 0 22 20" aria-label="Warning"><path d="M11 1L21 19H1Z" fill="#fff"/><path d="M11 7v6" stroke="#0d0e10" stroke-width="2.2"/><circle cx="11" cy="16" r="1.2" fill="#0d0e10"/></svg>
      <svg width="16" height="18" viewBox="0 0 16 20" aria-label="Dispose properly"><path d="M3 8h10l-1.2 11H4.2Z" fill="none" stroke="#fff" stroke-width="1.4"/><path d="M2 6h12M8 1v4M5.5 3L8 1l2.5 2" fill="none" stroke="#fff" stroke-width="1.4"/></svg>
    </div>
    <div class="footer"><span>MANUFACTURED BY:</span><span class="footer__origin">MADE IN<br>NEW ZEALAND</span></div>
  </article>

</main>
</body>
</html>
```